New Corporate Email footer (business card design) for 40th Anniversary for Timber Traders

We are traders in sustainable timber worldwide, specialising in tropical hardwoods.
We need to keep our current company logo, but update our email footer with a business card like design which marks the company's 40th Anniversary. 1981-2021. We would need:
Company Logo, Name and Address, website
Sender's: Name, Tel no, fax no, email address
We would need this in a format which we could update ourselves re names/phone numbers if any change.

Target Market(s)

Customers, suppliers, service providers

Contact Information for Business Card

Maria Penhale
Tel: +44 (0) 208 497 3316
Fax: +44 (0) 208 497 2284
Email: maria@rwltimber.example.co.uk
Web: www.rwltimber.example.co.uk

RWL Timber Ltd. 17 Marlow Court, Ashby Crescent, Sanderstead, Surrey KT7 4PZ, UNITED KINGDOM

IMPORTANT NOTICE - This message contains confidential information for the intended addressee only. Any views expressed are those of the sender not RWL Timber Ltd unless otherwise stated. If you receive this message [and any attachment(s)] in error you must not store, copy, disclose or otherwise use any part of it and should advise the sender immediately on 020 8497 5162. Internet communications are not guaranteed secure or virus free. RWL reserves the right to monitor all e-mail communications and does not accept responsibility for any loss or damage resulting from access of this e-mail or any file(s) attached.

Font styles to use
Sans Serif
Other font styles liked:
• not actually sure

Requirements
Must have
• mention of company's 40th Anniversary 1981-2021, which is the whole point of the design
Nice to have
• Our company colour is British Racing Green, but any green theme may be good
Maybe a tree design but allowing the company logo to stand out.

```html
<!DOCTYPE html>
<html lang="en">
<head>
<meta charset="utf-8">
<title>RWL Timber – 40th Anniversary Business Card</title>
<link rel="stylesheet" href="https://fonts.googleapis.com/css2?family=Archivo+Black&family=Arimo:wght@400;700&display=swap">
<style>
  :root {
    --stage: #2a2a2c;
    --ink: #111111;
    --paper: #ffffff;
    --gold-light: #fbe9a0;
    --gold-mid: #eab54a;
    --gold-deep: #d9892e;
    --rule: #333333;
  }
  * { box-sizing: border-box; margin: 0; padding: 0; }
  html, body { width: 1200px; height: 900px; overflow: hidden; }
  body {
    background: var(--stage);
    position: relative;
    font-family: "Arimo", Arial, sans-serif;
  }
  .card {
    position: absolute;
    width: 640px;
    height: 370px;
    border-radius: 26px;
    overflow: hidden;
    box-shadow: 0 10px 28px rgba(0,0,0,.55);
  }

  /* Front – gold */
  .card-front {
    left: 70px; top: 80px;
    background: linear-gradient(110deg, var(--gold-deep) 0%, var(--gold-mid) 25%, var(--gold-light) 48%, var(--gold-mid) 72%, var(--gold-deep) 100%);
  }
  .card-front .texture {
    position: absolute; inset: 0;
    background: linear-gradient(160deg, rgba(255,255,255,.12) 0%, rgba(255,255,255,0) 40%, rgba(0,0,0,.06) 100%);
  }
  .brand {
    position: absolute;
    display: flex; align-items: center; gap: 14px;
    color: var(--ink);
    font-family: "Archivo Black", "Arial Black", sans-serif;
    letter-spacing: 2px;
  }
  .brand-dot { border-radius: 50%; background: var(--ink); }
  .card-front .brand { left: 50%; top: 50%; transform: translate(-50%, -50%); font-size: 64px; }
  .card-front .brand-dot { width: 70px; height: 70px; }

  /* Back – white */
  .card-back {
    left: 490px; top: 440px;
    background: var(--paper);
  }
  .card-back .brand { left: 215px; top: 70px; font-size: 54px; }
  .card-back .brand-dot { width: 58px; height: 58px; }

  .anniversary-badge {
    position: absolute; right: 40px; top: 22px;
    width: 86px; height: 86px; border-radius: 50%;
    background: #161616;
    border: 4px solid var(--gold-mid);
    display: flex; flex-direction: column; align-items: center; justify-content: center;
    color: var(--gold-mid);
  }
  .anniversary-badge .years { font-size: 8px; letter-spacing: .5px; }
  .anniversary-badge .number { font-family: "Archivo Black", sans-serif; font-size: 30px; line-height: 1; }
  .anniversary-badge .label { font-size: 7px; letter-spacing: 1px; }

  .person-name {
    position: absolute; left: 150px; top: 282px;
    font-family: "Archivo Black", "Arial Black", sans-serif;
    font-size: 24px; letter-spacing: 1.5px; color: var(--ink);
  }
  .divider {
    position: absolute; left: 390px; top: 215px;
    width: 1.5px; height: 115px; background: var(--rule);
  }
  .contact-list {
    position: absolute; left: 405px; top: 222px;
    list-style: none;
    font-size: 14px; color: var(--ink);
  }
  .contact-list li { display: flex; align-items: center; gap: 8px; height: 24px; }
  .contact-icon {
    width: 15px; height: 15px; border-radius: 3px; flex: none;
    background: linear-gradient(135deg, var(--gold-light), var(--gold-deep));
    display: flex; align-items: center; justify-content: center;
  }
  .contact-icon svg { width: 11px; height: 11px; }
</style>
</head>
<body>

  <section class="card card-front">
    <div class="texture" role="img" aria-label="Faint flag-style stripe pattern over the gold foil"></div>
    <div class="brand"><span class="brand-dot"></span>RWL</div>
  </section>

  <section class="card card-back">
    <div class="anniversary-badge">
      <span class="years">1981-2021</span>
      <span class="number">40</span>
      <span class="label">ANNIVERSARY</span>
    </div>

    <div class="brand"><span class="brand-dot"></span>RWL</div>

    <p class="person-name">MARIA PENHALE</p>
    <span class="divider"></span>

    <ul class="contact-list">
      <li>
        <span class="contact-icon"><svg viewBox="0 0 12 12"><path d="M3 1.5l1.5 2-1 1c.6 1.3 1.7 2.4 3 3l1-1 2 1.5-1 2C5 10 2 7 1.5 3z" fill="#fff"/></svg></span>
        +44 (0) 208 497 3316
      </li>
      <li>
        <span class="contact-icon"><svg viewBox="0 0 12 12"><rect x="3" y="1.5" width="6" height="3" fill="#fff"/><rect x="1.5" y="5" width="9" height="4.5" rx="1" fill="#fff"/></svg></span>
        +44 (0) 208 497 2284
      </li>
      <li>
        <span class="contact-icon"><svg viewBox="0 0 12 12"><rect x="1.5" y="3" width="9" height="6" fill="none" stroke="#fff" stroke-width="1.2"/><path d="M1.5 3L6 6.5 10.5 3" fill="none" stroke="#fff" stroke-width="1.2"/></svg></span>
        maria@rwltimber.example.co.uk
      </li>
      <li>
        <span class="contact-icon"><svg viewBox="0 0 12 12"><circle cx="6" cy="6" r="4.3" fill="none" stroke="#fff" stroke-width="1.1"/><path d="M1.7 6h8.6M6 1.7c-2 2.5-2 6.1 0 8.6M6 1.7c2 2.5 2 6.1 0 8.6" fill="none" stroke="#fff" stroke-width=".9"/></svg></span>
        www.rwltimber.example.co.uk
      </li>
    </ul>
  </section>

</body>
</html>
```